Packaging design for handmade soap

We are looking for a packaging design for a brand new product line: handmade soaps, called VELMO

We are looking for a design of an outer box together with the logo. We need the design for a 90x65x30mm box (see attached). We trying to get a high-end product preferable with vintage elements (but we don't want a shiny box, it will be finished with matte lacque, however logo or other certain elements could be shiny).

The design should reflect the fact that we have a handmade, all natural soap.

I uploaded a couple of packaging examples I like.

UPDATE 1: It also should have a title, which describes the product more accurate, like "Natural Soap with Seabuckthorn and Olive oil"

UPDATE 2: I would remove the expression "high-end" from the description if high end would mean a lot of flowers in the background. I would like if you would insist about the ideea of "natural" in your works

UPDATE 3: Prefered colors green and brown (which brings the ideea of nature, natural)

Target Market(s)

Women 20-45 years with above average income

Industry/Entity Type

Cosmetics

Font styles to use
Serif

Colors
9bcb3c
acd036
cadf82
f78f20
ffc214
f37122
fbed22
fece3e
faa54b

Requirements
Must have
• A literal representation of the brand VELMO (we don't have a logo for it)

```html
<!DOCTYPE html>
<html lang="en">
<head>
<meta charset="utf-8">
<title>VELMO handmade soap packaging</title>
<link href="https://fonts.googleapis.com/css2?family=Oranienbaum&family=PT+Sans+Narrow&family=Libre+Baskerville&display=swap" rel="stylesheet">
<style>
  :root {
    --canvas: #ffffff;
    --ink-brown: #5b4a2e;
    --yellow: #fdc93a;
    --green: #9bcb3c;
    --green-light: #cadf82;
    --cream: #f1e9a8;
    --bronze: #a97d4f;
    --gold: #d6b46c;
  }
  * { margin: 0; padding: 0; box-sizing: border-box; }
  html, body { width: 1200px; height: 942px; overflow: hidden; background: var(--canvas); }
  .canvas { position: relative; width: 1200px; height: 942px; }

  .soap-box {
    position: absolute; width: 485px; height: 350px;
    background:
      linear-gradient(to bottom, rgba(255,255,255,0.5), rgba(255,255,255,0) 26px),
      repeating-linear-gradient(to bottom, var(--tone) 0 6px, rgba(255,255,255,0.6) 6px 8px);
  }
  .soap-box--yellow { left: 70px; top: 78px; --tone: var(--yellow); --accent: var(--yellow); }
  .soap-box--green { left: 70px; top: 530px; --tone: var(--green-light); --accent: var(--green); }
  .soap-box--cream { left: 640px; top: 383px; --tone: var(--cream); --accent: var(--bronze); }

  .label {
    position: absolute; left: 100px; top: 0; width: 285px; height: 318px;
    background: linear-gradient(to bottom, #f0f0f0, #ffffff 22px);
    text-align: center;
  }
  .label::before {
    content: ""; position: absolute; left: 13px; right: 13px; top: 0; bottom: 13px;
    border: 1.5px solid var(--accent); border-top: none;
  }
  .brand {
    position: absolute; left: 0; right: 0; top: 52px;
    display: flex; align-items: center; justify-content: center; gap: 10px;
  }
  .brand-dot { width: 34px; height: 34px; border-radius: 50%; background: var(--accent); }
  .brand-name {
    font-family: "Oranienbaum", serif; font-size: 42px;
    color: var(--accent); letter-spacing: 1px; line-height: 1;
  }
  .product-title {
    position: absolute; left: 26px; right: 26px; top: 186px;
    font-family: "Oranienbaum", serif; font-weight: 400; font-size: 38px;
    color: var(--ink-brown); letter-spacing: 1px; line-height: 1;
    white-space: nowrap;
  }
  .ingredients {
    position: absolute; left: 33px; right: 33px; top: 232px; height: 27px;
    background: var(--accent); color: #fff;
    font-family: "PT Sans Narrow", sans-serif; font-size: 16px; line-height: 27px;
    white-space: nowrap;
  }
  .weight {
    position: absolute; left: 0; right: 0; top: 278px;
    font-family: "Libre Baskerville", serif; font-size: 12px; color: var(--ink-brown);
  }

  .brand-hero {
    position: absolute; left: 660px; top: 140px;
    display: flex; align-items: center; gap: 22px;
  }
  .brand-hero .brand-dot { width: 96px; height: 96px; background: var(--gold); }
  .brand-hero .brand-name { font-size: 110px; color: var(--gold); letter-spacing: 3px; }
</style>
</head>
<body>
<main class="canvas">

  <section class="soap-box soap-box--yellow">
    <div class="label">
      <div class="brand"><span class="brand-dot"></span><span class="brand-name">VELMO</span></div>
      <h2 class="product-title">NATURAL SOAP</h2>
      <p class="ingredients">with Seabuckthorn and Olive Oil</p>
      <p class="weight">4 oz.</p>
    </div>
  </section>

  <section class="soap-box soap-box--green">
    <div class="label">
      <div class="brand"><span class="brand-dot"></span><span class="brand-name">VELMO</span></div>
      <h2 class="product-title">NATURAL SOAP</h2>
      <p class="ingredients">with Seabuckthorn and Olive Oil</p>
      <p class="weight">4 oz.</p>
    </div>
  </section>

  <section class="soap-box soap-box--cream">
    <div class="label">
      <div class="brand"><span class="brand-dot"></span><span class="brand-name">VELMO</span></div>
      <h2 class="product-title">NATURAL SOAP</h2>
      <p class="ingredients">with Seabuckthorn and Olive Oil</p>
      <p class="weight">4 oz.</p>
    </div>
  </section>

  <div class="brand-hero">
    <span class="brand-dot"></span><span class="brand-name">VELMO</span>
  </div>

</main>
</body>
</html>
```